Business card design for Birch Engineering Torvant

We need a new business card design along with all the necessary to place an order. The company is Birch Engineering Torvant and we recently updated our logo.

```html
<!DOCTYPE html>
<html lang="en">
<head>
<meta charset="utf-8">
<title>Birch Engineering Torvant – Business Card</title>
<link rel="stylesheet" href="https://fonts.googleapis.com/css2?family=Poppins:wght@400;500;600;700&display=swap">
<style>
  :root {
    --paper: #ffffff;
    --stage: #ffffff;
    --stone: #939392;
    --stone-light: #e6e6e6;
    --gold: #e0bd2a;
    --gold-pale: #f6edd0;
    --ink-white: #ffffff;
  }
  * { box-sizing: border-box; margin: 0; padding: 0; }
  html, body {
    width: 979px;
    height: 1200px;
    overflow: hidden;
    background: var(--stage);
    font-family: "Poppins", sans-serif;
  }
  .canvas { position: relative; width: 979px; height: 1200px; }

  .card {
    position: absolute;
    left: 119px;
    width: 745px;
    height: 426px;
    background: var(--paper);
    overflow: hidden;
    box-shadow: 6px 8px 10px rgba(0,0,0,0.28);
  }
  .card--front { top: 140px; }
  .card--back { top: 648px; }

  .front-accent {
    position: absolute;
    left: 0; top: 0;
    width: 240px; height: 426px;
    background: linear-gradient(90deg, var(--gold-pale) 0%, rgba(246,237,208,0.5) 45%, rgba(230,230,230,0) 100%);
  }

  .wordmark {
    position: absolute;
    display: flex;
    align-items: center;
    gap: 12px;
    color: var(--stone);
    font-family: "Poppins", sans-serif;
    font-weight: 600;
  }
  .wordmark__square { background: var(--gold); flex: none; }
  .wordmark__text { display: flex; flex-direction: column; line-height: 1; }
  .wordmark__main { letter-spacing: 2px; }

  .card--front .wordmark { left: 50%; top: 174px; transform: translateX(-50%); }
  .card--front .wordmark__square { width: 34px; height: 34px; }
  .card--front .wordmark__main { font-size: 50px; }
  .card--front .wordmark__sub { font-size: 19px; letter-spacing: 0.5px; margin-top: 4px; }

  .card--back .wordmark { left: 40px; top: 68px; gap: 9px; }
  .card--back .wordmark__square { width: 26px; height: 26px; }
  .card--back .wordmark__main { font-size: 38px; }
  .card--back .wordmark__sub { font-size: 14.5px; letter-spacing: 0.3px; margin-top: 3px; }

  .info-band {
    position: absolute;
    left: 0; top: 189px;
    width: 745px; height: 237px;
    background: var(--stone);
  }
  .person__bar {
    position: absolute; left: 0; top: 271px;
    width: 6px; height: 60px;
    background: var(--gold);
  }
  .person {
    position: absolute; left: 38px; top: 278px;
    color: var(--ink-white);
  }
  .person__name { font-size: 24px; font-weight: 600; line-height: 1.1; }
  .person__role { font-size: 15px; font-weight: 400; line-height: 1.3; }

  .contact {
    position: absolute; left: 374px; top: 252px;
    list-style: none;
    color: var(--ink-white);
    font-size: 17px;
    line-height: 27px;
  }
  .contact__item { display: flex; align-items: flex-start; }
  .contact__icon { width: 20px; height: 27px; flex: none; margin-right: 13px; display: flex; align-items: center; justify-content: center; }
  .contact__icon svg { width: 17px; height: 17px; fill: var(--gold); }
</style>
</head>
<body>
<main class="canvas">

  <section class="card card--front" aria-label="Business card front">
    <div class="front-accent" role="img" aria-label="Soft gold and grey accent area at the card's left edge"></div>
    <div class="wordmark">
      <span class="wordmark__square"></span>
      <span class="wordmark__text">
        <span class="wordmark__main">BIRCH</span>
        <span class="wordmark__sub">ENGINEERING TORVANT</span>
      </span>
    </div>
  </section>

  <section class="card card--back" aria-label="Business card back">
    <div class="wordmark">
      <span class="wordmark__square"></span>
      <span class="wordmark__text">
        <span class="wordmark__main">BIRCH</span>
        <span class="wordmark__sub">ENGINEERING TORVANT</span>
      </span>
    </div>

    <div class="info-band"></div>
    <div class="person__bar"></div>
    <div class="person">
      <p class="person__name">Name Name</p>
      <p class="person__role">CEO</p>
    </div>

    <ul class="contact">
      <li class="contact__item">
        <span class="contact__icon"><svg viewBox="0 0 24 24"><path d="M6.6 10.8c1.4 2.8 3.8 5.1 6.6 6.6l2.2-2.2c.3-.3.7-.4 1-.2 1.1.4 2.3.6 3.6.6.6 0 1 .4 1 1V20c0 .6-.4 1-1 1C10.6 21 3 13.4 3 4c0-.6.4-1 1-1h3.5c.6 0 1 .4 1 1 0 1.3.2 2.5.6 3.6.1.3 0 .7-.2 1z"/></svg></span>
        <span>000-000-0000</span>
      </li>
      <li class="contact__item">
        <span class="contact__icon"><svg viewBox="0 0 24 24"><path d="M2 5h20v2.2l-10 6.3L2 7.2z M2 9.5l10 6.3 10-6.3V19H2z"/></svg></span>
        <span>info@birchtorvant.com</span>
      </li>
      <li class="contact__item">
        <span class="contact__icon"><svg viewBox="0 0 24 24"><path d="M12 2a10 10 0 1 0 0 20 10 10 0 0 0 0-20zm6.9 9h-3a15 15 0 0 0-1.3-5.5A8 8 0 0 1 18.9 11zM12 4.1c.9 1.2 1.8 3.5 2 6.9h-4c.2-3.4 1.1-5.7 2-6.9zM9.4 5.5A15 15 0 0 0 8.1 11h-3a8 8 0 0 1 4.3-5.5zM5.1 13h3a15 15 0 0 0 1.3 5.5A8 8 0 0 1 5.1 13zm6.9 6.9c-.9-1.2-1.8-3.5-2-6.9h4c-.2 3.4-1.1 5.7-2 6.9zm2.6-1.4a15 15 0 0 0 1.3-5.5h3a8 8 0 0 1-4.3 5.5z"/></svg></span>
        <span>birchtorvant.com</span>
      </li>
      <li class="contact__item">
        <span class="contact__icon"><svg viewBox="0 0 24 24"><path d="M12 2a7 7 0 0 0-7 7c0 5 7 13 7 13s7-8 7-13a7 7 0 0 0-7-7zm0 9.5A2.5 2.5 0 1 1 12 6.5a2.5 2.5 0 0 1 0 5z"/></svg></span>
        <span>3361 Address Street, City,<br>Country Zip code</span>
      </li>
    </ul>
  </section>

</main>
</body>
</html>
```